Pizza Restaurant Needs a New Menu Design

RESTAURANT NAME: The Oven and Barrel House
LOCATION:
- Kyneton, central Victoria Australia
- A small historical country town, with a growing market in visitors from Melbourne coming for food and local activities.
TYPE OF RESTAURANT
Pizza and Pasta restaurant. Modern feel, lots of timber, busy feel.
- Describe the overall restaurant theme/concept
- Ambiance
CLIENTELE:
- Mostly local clientele, but a growing number of tourists also. Local families and young people.
Describe your patrons or your market
OBJECTIVE:
-to give a more modern and professional feel to our menus. They are old and simple and boring.
- hard to read under low light at night.
Why are we updating the old menu?
- What do you like about the old menu that designers should keep or consider when designing
- What do you not like about the old menu?
ADDITIONAL INFORMATION:
www.ovenandbarrelhouse.com.au
https://www.facebook.com/The-Oven-and-Barrel-House-804417362958120/
RESOURCES/ SIZES:
Please find attached all our current menus as requested. With all attachments you will notice 2 of everything. We currently print each menu back to back on white card.
Restaurant 1 and Restaurant 2 - back to back - A3 and then folded
Red Wine and White Wine - back to back A4
Take away 1 and Take away 2 - back to back A4
Dessert - A4 - cut in half
Lunch Menu and Lunch Drink Menu - back to back A4
A3 Takeaway Menu
Thank you :)

```html
<!DOCTYPE html>
<html lang="en">
<head>
<meta charset="utf-8">
<title>Desserts Menu – The Oven and Barrel House</title>
<link rel="stylesheet" href="https://fonts.googleapis.com/css2?family=Bebas+Neue&family=Kaushan+Script&family=Quicksand:wght@300;400&display=swap">
<style>
  :root {
    --page-bg: #e7e3dd;
    --card-bg: #2a2a2c;
    --panel: rgba(255,255,255,0.17);
    --brand-red: #9b1b30;
    --white: #ffffff;
    --body-text: #e6e6e6;
    --ph-cake-a: #5e3a2c; --ph-cake-b: #4a2e24;
    --ph-cone-a: #e9dcc4; --ph-cone-b: #e3c48f;
    --ph-sundae-a: #8a6a5c; --ph-sundae-b: #9fc3c8;
  }
  html, body { margin: 0; padding: 0; width: 1200px; height: 1000px; overflow: hidden; background: var(--page-bg); }
  .menu-card {
    position: absolute; left: 260px; top: 57px; width: 648px; height: 918px;
    background: var(--card-bg); overflow: hidden;
    font-family: "Quicksand", sans-serif; color: var(--body-text);
  }
  .title-band { position: absolute; left: 0; top: 90px; width: 648px; height: 65px; background: var(--white); }
  .menu-title {
    position: absolute; left: 68px; top: 40px; margin: 0;
    font-family: "Kaushan Script", cursive; font-weight: 400; font-size: 100px; line-height: 1;
    color: var(--brand-red); white-space: nowrap;
  }
  .menu-tagline {
    position: absolute; left: 260px; top: 155px; margin: 0;
    font-family: "Bebas Neue", sans-serif; font-size: 22px; letter-spacing: 1.2px; color: var(--white);
  }
  .brand-badge {
    position: absolute; left: 460px; top: 27px; width: 172px; height: 172px; border-radius: 50%;
    background: var(--brand-red); box-sizing: border-box; border: 4px solid var(--white);
    display: flex; align-items: center; justify-content: center; text-align: center;
  }
  .brand-name { font-family: "Bebas Neue", sans-serif; font-size: 29px; line-height: 1; color: var(--white); width: 130px; }
  .panel { position: absolute; width: 340px; height: 140px; background: var(--panel);
    clip-path: polygon(22% 0, 100% 0, 78% 100%, 0 100%); }
  .panel-sticky { left: 13px; top: 248px; }
  .panel-crumble { left: 293px; top: 340px; }
  .panel-mousse { left: 8px; top: 491px; }
  .panel-cone { left: 268px; top: 576px; }
  .menu-item { position: absolute; }
  .item-name { margin: 0; font-family: "Bebas Neue", sans-serif; font-weight: 400; font-size: 29px; line-height: 26px; color: var(--white); letter-spacing: .3px; white-space: nowrap; }
  .item-desc { margin: 0; font-weight: 300; font-size: 18px; line-height: 18px; white-space: nowrap; letter-spacing: .2px; }
  .item-price { margin: 4px 0 0; font-family: "Bebas Neue", sans-serif; font-size: 22px; line-height: 22px; color: var(--white); letter-spacing: .5px; white-space: nowrap; }
  .item-sticky { left: 70px; top: 261px; }
  .item-crumble { left: 348px; top: 347px; }
  .item-crumble .item-desc, .item-mousse .item-desc, .item-cone .item-desc { line-height: 21px; margin-top: 7px; }
  .item-crumble .item-price, .item-mousse .item-price, .item-cone .item-price { margin-top: 7px; }
  .item-mousse { left: 70px; top: 504px; }
  .item-cone { left: 333px; top: 585px; }
  .feature-box { position: absolute; left: 148px; top: 738px; width: 350px; height: 180px; background: var(--brand-red); }
  .item-sundae { left: 20px; top: 8px; }
  .item-sundae .item-desc { font-size: 19px; line-height: 22px; margin-top: 8px; }
  .item-sundae .item-price { margin: 8px 0 0 4px; }
  .placeholder { position: absolute; border-radius: 4px; }
  .placeholder-cake { left: 150px; top: 341px; width: 135px; height: 110px;
    background: linear-gradient(180deg, var(--ph-cake-a), var(--ph-cake-b)); }
  .placeholder-cone { left: 545px; top: 533px; width: 85px; height: 215px;
    background: linear-gradient(180deg, var(--ph-cone-a), var(--ph-cone-b)); }
  .placeholder-sundae { left: 33px; top: 703px; width: 127px; height: 195px;
    background: linear-gradient(180deg, var(--ph-sundae-a), var(--ph-sundae-b)); }
</style>
</head>
<body>
<main class="menu-card">
  <div class="title-band"></div>
  <h1 class="menu-title">Desserts</h1>
  <p class="menu-tagline">Made in House</p>
  <div class="brand-badge"><span class="brand-name">The Oven and Barrel House</span></div>

  <div class="panel panel-sticky"></div>
  <div class="panel panel-crumble"></div>
  <div class="panel panel-mousse"></div>
  <div class="panel panel-cone"></div>

  <div class="placeholder placeholder-cake" role="img" aria-label="Illustration of a slice of layered chocolate cake"></div>
  <div class="placeholder placeholder-cone" role="img" aria-label="Illustration of a soft-serve vanilla ice cream cone with sprinkles"></div>
  <div class="placeholder placeholder-sundae" role="img" aria-label="Illustration of an ice cream sundae with chocolate sauce and a cherry"></div>

  <section class="menu-item item-sticky">
    <h2 class="item-name">Sticky Date Pudding</h2>
    <p class="item-desc">with butterscotch<br>sauce, cream and/or<br>ice cream</p>
    <p class="item-price">$8.00</p>
  </section>
  <section class="menu-item item-crumble">
    <h2 class="item-name">Apple Crumble</h2>
    <p class="item-desc">Juicy apples slices baked<br>with crumble,topped with<br>cream and/ or ice cream</p>
    <p class="item-price">$8.00</p>
  </section>
  <section class="menu-item item-mousse">
    <h2 class="item-name">Chocolate Mousse</h2>
    <p class="item-desc">Rich creamy chocolate<br>mousse served with<br>cream</p>
    <p class="item-price">$8.00</p>
  </section>
  <section class="menu-item item-cone">
    <h2 class="item-name">Ice Cream Cone</h2>
    <p class="item-desc">Scoop of Vanilla Ice<br>Cream in a cone<br>(sprinkles oaptional)</p>
    <p class="item-price">$2.00</p>
  </section>
  <div class="feature-box">
    <section class="menu-item item-sundae">
      <h2 class="item-name">Ice Cream Sundae</h2>
      <p class="item-desc">Scoops of Vanilla Ice cream<br>served withchoice of toppings<br>Chocolate, Strawberry or Caramel<br>(Sprinkles optional )</p>
      <p class="item-price">$8.00 (Kids size - $6.00)</p>
    </section>
  </div>
</main>
</body>
</html>
```